Web Design Project

We are re-starting this project.

This project is for a totally new look and design of a website for Wablor. www.wablor-demo.net.

Wablor is a naming protocol for physical locations and can be used for fixed and mobile people, places and things. Find your friends, or find a business. Because Wablor locations point to precise geo-physical (GPS) co-ordinates, navigation to a location becomes totally reliable.
Updates

Please see the modified brief for this project

Target Market(s)

Every person and every business can have multiple !Wabs (Wablor locations), so the website needs to be appealing and fun, but easy to use and functional

Industry/Entity Type

Business

Colors
34a6d7

Requirements
Must have
• Uniqueness!

```html
<!DOCTYPE html>
<html lang="en">
<head>
<meta charset="utf-8">
<title>Wablor</title>
<link rel="stylesheet" href="https://fonts.googleapis.com/css2?family=Comfortaa:wght@400;700&family=Open+Sans:wght@400;600&display=swap">
<style>
:root{
  --brand:#1e98d6;
  --brand-soft:#2aa2dc;
  --accent:#e04a22;
  --ink:#595e63;
  --slate:#434b52;
  --white:#ffffff;
  --panel:rgba(246,247,249,0.93);
}
*{box-sizing:border-box;margin:0;padding:0}
html,body{width:980px;height:1200px;overflow:hidden;background:var(--white)}
body{position:relative;font-family:"Open Sans",Arial,sans-serif;color:var(--ink)}
.site-header{position:absolute;left:0;top:0;width:980px;height:100px;background:var(--brand)}
.brand{position:absolute;left:96px;top:26px;display:flex;align-items:center;gap:8px;color:var(--white);font-family:"Comfortaa",Arial,sans-serif;font-weight:700;font-size:34px;letter-spacing:-0.5px}
.brand-dot{width:18px;height:18px;border-radius:50%;background:var(--white)}
.main-nav{position:absolute;right:90px;top:43px;display:flex;gap:15px}
.main-nav a{color:var(--white);text-decoration:none;font-size:12px}
.hero{position:absolute;left:0;top:100px;width:980px;height:446px}
.hero-photo{position:absolute;inset:0;background:linear-gradient(90deg,#3a3f45 0%,#8d98a4 30%,#b9c3cc 55%,#9aa6b1 80%,#c6ced6 100%)}
.finder{position:absolute;left:619px;top:55px;width:271px}
.finder-top{background:var(--brand);height:150px;padding:30px 16px 0 16px;position:relative}
.finder-title{position:absolute;left:76px;top:30px;color:var(--white);font-family:"Comfortaa",Arial,sans-serif;font-size:18px;line-height:24px}
.finder-icon{position:absolute;left:20px;top:31px}
.search{position:absolute;left:16px;top:85px;width:240px;height:37px;background:var(--white);display:flex;align-items:center;justify-content:space-between;padding:0 12px 0 15px}
.search span{font-size:11.5px;color:var(--brand)}
.finder-body{background:var(--panel);height:209px;padding:28px 19px 0 19px;position:relative}
.finder-body h2{font-family:"Comfortaa",Arial,sans-serif;font-weight:400;color:var(--brand);font-size:17.5px;line-height:24px}
.finder-body h2 strong{font-weight:700}
.finder-body p{margin-top:10px;font-size:10.6px;line-height:14px;color:var(--ink)}
.arrow{position:absolute;top:165px}
.arrow.prev{left:16px}.arrow.next{right:16px}
.activity{position:absolute;left:0;top:546px;width:980px;height:441px}
.update{position:absolute;width:400px;height:68px}
.update svg{position:absolute;left:0;top:0}
.update p{position:absolute;left:67px;top:31px;font-size:15.4px;line-height:18px;white-space:nowrap}
.handle{color:var(--brand)}
.place{color:var(--accent)}
.cta{position:absolute;left:0;top:987px;width:980px;height:161px;background:var(--brand);text-align:center}
.cta p{position:absolute;left:0;right:0;top:32px;color:var(--white);font-family:"Comfortaa",Arial,sans-serif;font-size:14px}
.join{position:absolute;left:379px;top:71px;width:222px;height:53px;background:var(--slate);color:var(--white);font-family:"Comfortaa",Arial,sans-serif;font-size:28px;line-height:52px;letter-spacing:-0.5px}
.site-footer{position:absolute;left:0;top:1148px;width:980px;height:52px;background:var(--slate)}
.footer-links{position:absolute;left:96px;top:19px;display:flex;gap:12px}
.footer-links a{color:var(--white);text-decoration:none;font-size:11px}
.powered{position:absolute;right:111px;top:13px;display:flex;align-items:center;gap:10px;color:var(--white);font-size:11px}
.powered strong{font-family:"Comfortaa",Arial,sans-serif;font-weight:700;font-size:17px}
</style>
</head>
<body>
<header class="site-header">
  <div class="brand"><span class="brand-dot"></span>Wablor</div>
  <nav class="main-nav"><a href="#">SIGN UP</a><a href="#">LOGIN</a></nav>
</header>

<section class="hero">
  <div class="hero-photo" role="img" aria-label="Photo of a traveller using a tablet in an airport lounge"></div>
  <div class="finder">
    <div class="finder-top">
      <svg class="finder-icon" width="42" height="42" viewBox="0 0 42 42" fill="none" stroke="#fff" stroke-width="3" stroke-linejoin="round">
        <path d="M21 3a9 9 0 0 1 9 9c0 7-9 16-9 16s-9-9-9-16a9 9 0 0 1 9-9z"/>
        <circle cx="21" cy="12" r="3.2"/>
        <path d="M3 37l8-8h6l-4 8zM25 29h6l8 8H29z" stroke-width="2.4"/>
      </svg>
      <div class="finder-title">Who would you like<br>to find?</div>
      <div class="search">
        <span>enter !wab...</span>
        <svg width="22" height="22" viewBox="0 0 22 22" fill="none" stroke="#1e98d6" stroke-width="3"><circle cx="9" cy="9" r="6.5"/><path d="M14 14l6 6" stroke-linecap="round"/></svg>
      </div>
    </div>
    <div class="finder-body">
      <h2>Save and manage your <strong>important personal locations.</strong></h2>
      <p>Home, work, favourite fishing or camping spot or any physical location on earth! Wablor is your address for life.</p>
      <svg class="arrow prev" width="29" height="29" viewBox="0 0 29 29" fill="none" stroke="#1e98d6" stroke-width="2.5"><circle cx="14.5" cy="14.5" r="12.5"/><path d="M16.5 9l-5.5 5.5 5.5 5.5" stroke-linecap="round"/></svg>
      <svg class="arrow next" width="29" height="29" viewBox="0 0 29 29" fill="none" stroke="#1e98d6" stroke-width="2.5"><circle cx="14.5" cy="14.5" r="12.5"/><path d="M12.5 9l5.5 5.5-5.5 5.5" stroke-linecap="round"/></svg>
    </div>
  </div>
</section>

<section class="activity">
  <div class="update" style="left:98px;top:58px">
    <svg width="54" height="68" viewBox="0 0 54 68"><path d="M27 2a25 25 0 0 1 25 25c0 16-25 40-25 40S2 43 2 27A25 25 0 0 1 27 2z" fill="#1e98d6"/><circle cx="27" cy="26" r="20" fill="#fff"/><circle cx="27" cy="26" r="17.5" fill="#b88f7c" role="img" aria-label="Member avatar"/></svg>
    <p><span class="handle">!mirelle</span> updated their current location<br><span class="place">!mirelle.now</span> 7 hours ago</p>
  </div>
  <div class="update" style="left:515px;top:58px">
    <svg width="54" height="68" viewBox="0 0 54 68"><path d="M27 2a25 25 0 0 1 25 25c0 16-25 40-25 40S2 43 2 27A25 25 0 0 1 27 2z" fill="#1e98d6"/><circle cx="27" cy="26" r="20" fill="#fff"/><circle cx="27" cy="26" r="17.5" fill="#a08a72" role="img" aria-label="Member avatar"/></svg>
    <p><span class="handle">!tessaroy</span> updated their current location<br><span class="place">!tessaroy.now</span> 12 hours ago</p>
  </div>
  <div class="update" style="left:98px;top:166px">
    <svg width="54" height="68" viewBox="0 0 54 68"><path d="M27 2a25 25 0 0 1 25 25c0 16-25 40-25 40S2 43 2 27A25 25 0 0 1 27 2z" fill="#1e98d6"/><circle cx="27" cy="26" r="20" fill="#fff"/><circle cx="27" cy="26" r="17.5" fill="#8a6a58" role="img" aria-label="Member avatar"/></svg>
    <p><span class="handle">!orlan</span> updated their current location<br><span class="place">!orlan.now</span> 14 hours ago</p>
  </div>
  <div class="update" style="left:515px;top:166px">
    <svg width="54" height="68" viewBox="0 0 54 68"><path d="M27 2a25 25 0 0 1 25 25c0 16-25 40-25 40S2 43 2 27A25 25 0 0 1 27 2z" fill="#1e98d6"/><circle cx="27" cy="26" r="20" fill="#fff"/><circle cx="27" cy="26" r="17.5" fill="#7a4a4e" role="img" aria-label="Member avatar"/></svg>
    <p><span class="handle">!kestrel88</span> added a location<br><span class="place">!kestrel88.home</span> 15 hours ago</p>
  </div>
  <div class="update" style="left:98px;top:275px">
    <svg width="54" height="68" viewBox="0 0 54 68"><path d="M27 2a25 25 0 0 1 25 25c0 16-25 40-25 40S2 43 2 27A25 25 0 0 1 27 2z" fill="#1e98d6"/><circle cx="27" cy="26" r="20" fill="#fff"/><circle cx="27" cy="26" r="17.5" fill="#b88f7c" role="img" aria-label="Member avatar"/></svg>
    <p><span class="handle">!mirelle</span> updated their current location<br><span class="place">!mirelle.now</span> 7 hours ago</p>
  </div>
  <div class="update" style="left:515px;top:275px">
    <svg width="54" height="68" viewBox="0 0 54 68"><path d="M27 2a25 25 0 0 1 25 25c0 16-25 40-25 40S2 43 2 27A25 25 0 0 1 27 2z" fill="#1e98d6"/><circle cx="27" cy="26" r="20" fill="#fff"/><circle cx="27" cy="26" r="17.5" fill="#a08a72" role="img" aria-label="Member avatar"/></svg>
    <p><span class="handle">!tessaroy</span> updated their current location<br><span class="place">!tessaroy.now</span> 12 hours ago</p>
  </div>
</section>

<section class="cta">
  <p>Lorem ipsum dolor sit amet, consectetur adipisicing elit, sed do eiusmod tempor incidore magna aliqua.</p>
  <div class="join">join now</div>
</section>

<footer class="site-footer">
  <nav class="footer-links"><a href="#">About</a><a href="#">Help</a><a href="#">Contact</a><a href="#">Privacy</a><a href="#">Terms</a><a href="#">Refunds</a><a href="#">Faq</a></nav>
  <div class="powered">Powered by <strong>Wablor</strong></div>
</footer>
</body>
</html>
```